Yacht Charter Broker needs a magazine page design

We are a travel agent for yachts called Velmora Yacht Charters. www.velmoracharters.example We are advertising in a magazine at the grand invitational trotter pony fair - https://gipfairground.example/ - and need a high-end luxury feeling magazine page.

Target Market(s)

Vacation goers looking to charter a crewed yacht.

Industry/Entity Type

Travel Agent

Requirements
Must have
• luxury feel. logo. website and social media icons if you feel necessary. Our motto is: Inhale. Exhale. Sail.
• Catamaran picture, snorkeling and other island, water looking pictures.
Nice to have
• Open to your design.
Should not have
• Nothing comes to mind.

```html
<!DOCTYPE html>
<html lang="en">
<head>
<meta charset="utf-8">
<title>Velmora Yacht Charters – Magazine Page</title>
<link href="https://fonts.googleapis.com/css2?family=Montserrat:wght@300;400;600&display=swap" rel="stylesheet">
<style>
  :root {
    --backdrop: #efeae1;
    --sea-light: #3f8fbf;
    --sea-mid: #2f73a3;
    --sea-deep: #1f5583;
    --navy: #13294f;
    --white: #ffffff;
    --text-soft: #d9e2ef;
  }
  * { margin: 0; padding: 0; box-sizing: border-box; }
  html, body { width: 1200px; height: 801px; overflow: hidden; }
  body {
    background: var(--backdrop);
    font-family: "Montserrat", sans-serif;
    color: var(--white);
  }
  .ad-page {
    position: absolute;
    left: 288px; top: 20px;
    width: 624px; height: 761px;
    background: var(--navy);
    overflow: hidden;
  }
  .ad-backdrop { position: absolute; inset: 0; }
  .motto-frame {
    position: absolute;
    left: 52px; top: 82px;
    width: 206px; height: 170px;
    border: 1.5px solid var(--white);
    padding: 22px 20px 0 24px;
    line-height: 1;
  }
  .motto-line {
    display: block;
    font-weight: 300;
    font-size: 34px;
    letter-spacing: 0.5px;
    margin-bottom: 4px;
  }
  .motto-sail {
    display: block;
    font-weight: 600;
    font-size: 54px;
    letter-spacing: 1px;
    margin-top: 4px;
  }
  .photo-circle {
    position: absolute;
    border-radius: 50%;
    border: 6px solid var(--white);
    box-shadow: 0 4px 10px rgba(0,0,0,0.35);
  }
  .circle-snorkel {
    left: 36px; top: 330px; width: 168px; height: 168px;
    background: radial-gradient(circle at 40% 35%, #7fc6d6, #2f8aa6 60%, #1d5f78);
  }
  .circle-seafood {
    left: 224px; top: 346px; width: 168px; height: 168px;
    background: radial-gradient(circle at 50% 40%, #f1e8e2, #d46a4a 55%, #8c8f96);
  }
  .circle-island {
    left: 412px; top: 296px; width: 160px; height: 160px;
    background: radial-gradient(circle at 45% 50%, #e9e4d3, #6fb3a7 50%, #2d8fb0);
  }
  .intro-copy {
    position: absolute;
    left: 58px; top: 560px;
    width: 508px;
    font-size: 11px;
    font-weight: 300;
    line-height: 1.55;
    text-align: justify;
    text-align-last: center;
    color: var(--text-soft);
  }
  .brand {
    position: absolute;
    left: 0; right: 0; top: 650px;
    text-align: center;
  }
  .brand-name {
    font-size: 24px;
    font-weight: 300;
    letter-spacing: 5px;
  }
  .brand-tagline {
    font-size: 6.5px;
    font-weight: 300;
    letter-spacing: 2.5px;
    margin-top: 2px;
  }
  .brand-rule {
    width: 190px;
    height: 1px;
    background: rgba(255,255,255,0.6);
    margin: 10px auto 7px;
  }
  .contact-line {
    font-size: 9px;
    font-weight: 300;
    line-height: 1.5;
  }
</style>
</head>
<body>
  <main class="ad-page">
    <svg class="ad-backdrop" width="624" height="761" viewBox="0 0 624 761" role="img" aria-label="Aerial photograph of clear blue sea with a white sailing yacht and a family standing at its bow">
      <defs>
        <linearGradient id="sea" x1="0" y1="0" x2="1" y2="1">
          <stop offset="0" stop-color="#2f73a3"/>
          <stop offset="0.5" stop-color="#3f8fbf"/>
          <stop offset="1" stop-color="#2a6a9b"/>
        </linearGradient>
      </defs>
      <rect width="624" height="761" fill="var(--navy)"/>
      <path d="M0 0 H624 V300 C520 330 420 340 300 360 C180 380 80 400 0 420 Z" fill="url(#sea)"/>
    </svg>

    <div class="motto-frame">
      <span class="motto-line">INHALE,</span>
      <span class="motto-line">EXHALE,</span>
      <span class="motto-sail">SAIL</span>
    </div>

    <div class="photo-circle circle-snorkel" role="img" aria-label="Photograph of a snorkeler swimming among tropical fish over a reef"></div>
    <div class="photo-circle circle-seafood" role="img" aria-label="Photograph of fresh lobster, fish and shrimp on ice"></div>
    <div class="photo-circle circle-island" role="img" aria-label="Aerial photograph of a small palm-covered island with white sand"></div>

    <p class="intro-copy">Great companies start with great people. You will find that your advisor at Velmora is collaborative, down-to-earth and open to the new. We build relationships on trust, consideration and integrity. We bring an incredible blend of services and technology to help finding you the vacation of a lifetime. You are going to love working with us.</p>

    <div class="brand">
      <div class="brand-name">VELMORA</div>
      <div class="brand-tagline">YACHT CHARTER BROKER</div>
      <div class="brand-rule"></div>
      <div class="contact-line">Grant: 555.010.0195 | Helena: 555.010.0196</div>
      <div class="contact-line">www.velmoracharters.example</div>
    </div>
  </main>
</body>
</html>
```